Business Card Design

Hoping for a black background business card, minimalistic design.
With the Marble Crest logo you created in white.

I would like to include:
My Name and title
Address (street address)
Reception: (phone number)
Fax: (fax number)
Reception: (email address)
Direct email: (email address)
Instagram: (ig handle)

```html
<!DOCTYPE html>
<html lang="en">
<head>
<meta charset="utf-8">
<title>Marble Crest – Business Card</title>
<link rel="stylesheet" href="https://fonts.googleapis.com/css2?family=Montserrat:wght@400;500;700&display=swap">
<style>
  :root {
    --bg-light: #e6e6e6;
    --bg-dark: #8c8c8c;
    --card-black: #1c1a1b;
    --card-charcoal: #4a4a4c;
    --panel-gray-light: #9a9b9e;
    --panel-gray-dark: #5e5f62;
    --swoosh-gray: #6d6e71;
    --swoosh-white: #ececec;
    --ink-white: #ffffff;
    --ink-soft: #ececec;
  }
  * { box-sizing: border-box; margin: 0; padding: 0; }
  html, body { width: 1200px; height: 1200px; overflow: hidden; }
  body {
    background: linear-gradient(110deg, var(--bg-light) 0%, #c4c4c4 55%, var(--bg-dark) 100%);
    font-family: "Montserrat", sans-serif;
    position: relative;
  }
  .card {
    position: absolute;
    left: 180px;
    width: 840px;
    height: 480px;
    border-radius: 30px;
    overflow: hidden;
  }
  .card-front {
    top: 90px;
    background: linear-gradient(100deg, #5a5a5c 0%, #2b2a2b 40%, var(--card-black) 70%, #111010 100%);
  }
  .card-back { top: 630px; }
  .card-back .art { position: absolute; inset: 0; }

  .lockup {
    position: absolute;
    display: flex;
    align-items: center;
    color: var(--ink-white);
    font-weight: 500;
    text-transform: uppercase;
    white-space: nowrap;
  }
  .lockup .dot {
    border: 4px solid var(--ink-white);
    border-radius: 50%;
    flex: none;
  }
  .card-front .lockup { left: 120px; top: 180px; gap: 34px; font-size: 52px; letter-spacing: 0.12em; }
  .card-front .lockup .dot { width: 112px; height: 112px; border-width: 6px; }
  .card-back .lockup { left: 512px; top: 210px; gap: 14px; font-size: 22px; letter-spacing: 0.12em; }
  .card-back .lockup .dot { width: 50px; height: 50px; border-width: 3px; }

  .details { position: absolute; left: 56px; top: 70px; color: var(--ink-white); }
  .details .name { font-size: 36px; font-weight: 700; }
  .details .role { font-size: 18px; font-weight: 400; color: var(--ink-soft); margin: 4px 0 0 14px; }
  .details .address { font-size: 20px; margin: 34px 0 14px 40px; color: var(--ink-soft); }
  .contacts { list-style: none; margin-left: 40px; }
  .contacts li { display: flex; align-items: center; gap: 12px; font-size: 20px; height: 34px; color: var(--ink-soft); }
  .contacts .icon {
    width: 24px; height: 24px; border-radius: 50%;
    background: var(--ink-white); flex: none;
    display: flex; align-items: center; justify-content: center;
  }
  .contacts .icon svg { width: 14px; height: 14px; }
</style>
</head>
<body>

<section class="card card-front" aria-label="Card front">
  <div class="lockup"><span class="dot"></span><span class="brand">Marble Crest</span></div>
</section>

<section class="card card-back" aria-label="Card back">
  <svg class="art" viewBox="0 0 840 480" aria-hidden="true">
    <defs>
      <linearGradient id="panel" x1="0" y1="0" x2="1" y2="0.3">
        <stop offset="0" stop-color="#9a9b9e"/>
        <stop offset="1" stop-color="#5e5f62"/>
      </linearGradient>
    </defs>
    <rect width="840" height="480" fill="url(#panel)"/>
    <ellipse cx="885" cy="206" rx="502" ry="412" fill="#6d6e71"/>
    <ellipse cx="889" cy="204" rx="490" ry="408" fill="#111"/>
    <ellipse cx="892" cy="203" rx="484" ry="406" fill="#ececec"/>
    <ellipse cx="899" cy="201" rx="474" ry="402" fill="#111"/>
    <ellipse cx="902" cy="200" rx="470" ry="400" fill="#1c1a1b"/>
  </svg>

  <div class="details">
    <p class="name">Dorian Vale</p>
    <p class="role">Manager</p>
    <p class="address">482 Linden Ave, Ottawa</p>
    <ul class="contacts">
      <li><span class="icon"><svg viewBox="0 0 16 16"><path d="M4 1.5l2.2 2.8-1.3 1.6a8 8 0 0 0 5.2 5.2l1.6-1.3 2.8 2.2-1.4 2.2C7 14 2 9 1.8 2.9z" fill="#5e5f62"/></svg></span>555-210-4387</li>
      <li><span class="icon"><svg viewBox="0 0 16 16"><rect x="4" y="1.5" width="8" height="4" fill="#5e5f62"/><rect x="1.5" y="6" width="13" height="6" rx="1" fill="#5e5f62"/><rect x="4" y="10" width="8" height="4.5" fill="#fff" stroke="#5e5f62"/></svg></span>555.318.2094</li>
      <li><span class="icon"><svg viewBox="0 0 16 16"><rect x="1.5" y="3.5" width="13" height="9" rx="1" fill="#5e5f62"/><path d="M2 4l6 5 6-5" fill="none" stroke="#fff" stroke-width="1.3"/></svg></span>info@marblecrest.com</li>
      <li><span class="icon"><svg viewBox="0 0 16 16"><circle cx="8" cy="8" r="6.5" fill="none" stroke="#5e5f62" stroke-width="1.4"/><ellipse cx="8" cy="8" rx="2.8" ry="6.5" fill="none" stroke="#5e5f62" stroke-width="1.2"/><path d="M1.5 8h13" stroke="#5e5f62" stroke-width="1.2"/></svg></span>www.marblecrest.com</li>
      <li><span class="icon"><svg viewBox="0 0 16 16"><circle cx="8" cy="8" r="5" fill="#5e5f62"/></svg></span>@marblecrest</li>
    </ul>
  </div>

  <div class="lockup"><span class="dot"></span><span class="brand">Marble Crest</span></div>
</section>

</body>
</html>
```